Soccer Training for Boys and Girls

I need like a flyer to post on facebook and instagram.
This is what O want to have on it.
you can use any color , soccer field on the background , or any soccer pictures.
Recreational and Travel Teams
Ages :5 to 14 years old
Field: Holloway Fenwick Middle School (4728 Meadowlark dr Silver spring, MD 20731)
Register online www.valmontekickers.example
-passing
-kicking
-shooting
-dribbling
-ball Control
Registration :$210 (includes 1st month, registration, practice Uniform
after 1st month.

Call us Phone:(240)555-0187

• kids playing soccer , soccer fields

```html
<!DOCTYPE html>
<html lang="en">
<head>
<meta charset="utf-8">
<title>Soccer Training — Boys and Girls</title>
<link rel="stylesheet" href="https://fonts.googleapis.com/css2?family=Passion+One:wght@700&family=Montserrat:wght@500;600;700;800&display=swap">
<style>
  :root {
    --night: #07080d;
    --navy: #0b1a3c;
    --royal: #1a3f7f;
    --band-blue: #1d5aa1;
    --band-white: #eeeeee;
    --white: #ffffff;
    --ink: #0a0a0a;
    --turf: #2c3a1c;
    --turf-dark: #141a10;
  }
  * { margin: 0; padding: 0; box-sizing: border-box; }
  html, body { width: 846px; height: 1200px; overflow: hidden; background: var(--night); }
  .flyer {
    position: relative; width: 846px; height: 1200px; overflow: hidden;
    background:
      radial-gradient(ellipse 520px 60px at 423px 178px, rgba(210,220,240,.55), transparent 70%),
      radial-gradient(ellipse 700px 260px at 423px 60px, #16275a, transparent 75%),
      linear-gradient(180deg, #0a1430 0%, #0a1022 25%, var(--night) 45%, var(--night) 100%);
    font-family: "Montserrat", sans-serif; color: var(--white);
  }
  .action-photo {
    position: absolute; left: 0; top: 492px; width: 846px; height: 460px;
    background: linear-gradient(180deg, rgba(7,8,13,.95) 0%, rgba(20,26,16,.6) 30%, var(--turf) 55%, var(--turf-dark) 85%, var(--night) 100%);
  }
  .shapes { position: absolute; inset: 0; }
  .brand {
    position: absolute; left: 0; width: 846px; top: 140px;
    font-weight: 800; font-size: 22px; letter-spacing: 1px;
    display: flex; justify-content: center; align-items: center; gap: 10px;
  }
  .brand-dot { width: 18px; height: 18px; border-radius: 50%; background: var(--band-blue); }
  .ages-label {
    position: absolute; left: 590px; top: 186px; width: 150px; text-align: center;
    font-weight: 800; font-size: 34px; letter-spacing: 1px;
  }
  .ages-range {
    position: absolute; right: 35px; top: 247px;
    font-weight: 600; font-size: 31px; letter-spacing: 1px;
  }
  .headline {
    position: absolute; width: 846px; text-align: center;
    font-family: "Passion One", sans-serif; font-weight: 700; line-height: 1; letter-spacing: 3px;
  }
  .headline--training { left: 26px; top: 314px; font-size: 78px; color: var(--white); }
  .headline--audience { left: 0; top: 401px; font-size: 80px; color: var(--ink); }
  .programs, .skills {
    position: absolute; left: 235px; width: 480px; text-align: center;
    font-family: "Passion One", sans-serif; font-weight: 700; font-size: 34px; line-height: 40px; letter-spacing: 1px;
  }
  .programs { top: 514px; }
  .skills { top: 638px; word-spacing: 14px; }
  .field-label { position: absolute; left: 42px; top: 800px; font-weight: 800; font-size: 30px; }
  .field-address {
    position: absolute; left: 199px; top: 810px; width: 540px;
    font-weight: 600; font-size: 25px; line-height: 35px;
  }
  .register {
    position: absolute; left: 38px; top: 938px;
    font-family: "Passion One", sans-serif; font-weight: 700; font-size: 46px; line-height: 57px; letter-spacing: 1px;
  }
  .site {
    position: absolute; left: 300px; top: 967px; width: 520px; text-align: center;
    font-weight: 700; font-size: 29px;
  }
  .price { position: absolute; left: 291px; top: 1052px; font-weight: 700; font-size: 25px; }
  .price-note {
    position: absolute; left: 292px; top: 1092px; width: 520px;
    font-weight: 500; font-size: 21px; line-height: 30px;
  }
  .phone {
    position: absolute; left: 292px; top: 1158px;
    font-weight: 700; font-size: 21px; line-height: 28px;
  }
</style>
</head>
<body>
<main class="flyer">
  <div class="action-photo" role="img" aria-label="Photo of young players competing for the ball on a stadium pitch at night"></div>

  <svg class="shapes" width="846" height="1200" viewBox="0 0 846 1200" aria-hidden="true">
    <polygon points="588,173 761,173 738,238 565,238" fill="var(--royal)" stroke="var(--white)" stroke-width="2"/>
    <polygon points="765,173 846,173 846,238 742,238" fill="var(--night)" stroke="var(--white)" stroke-width="2"/>
    <polygon points="73,310 821,310 805,395 54,395" fill="var(--band-blue)"/>
    <polygon points="64,395 839,395 816,482 48,482" fill="var(--band-white)"/>
    <polygon points="0,786 168,786 152,851 0,851" fill="var(--royal)" stroke="var(--white)" stroke-width="2"/>
    <polygon points="170,785 769,785 733,903 131,903" fill="var(--night)" stroke="var(--white)" stroke-width="2.5"/>
    <line x1="0" y1="987" x2="293" y2="987" stroke="var(--white)" stroke-width="2"/>
    <polygon points="298,953 846,953 846,1021 277,1021" fill="var(--royal)" stroke="var(--white)" stroke-width="2"/>
  </svg>

  <div class="brand"><span class="brand-dot"></span>Valmonte Kickers Academy</div>

  <div class="ages-label">AGES</div>
  <div class="ages-range">5 to 14 years old</div>

  <h1 class="headline headline--training">SOCCER TRAINING</h1>
  <h2 class="headline headline--audience">BOYS AND GIRLS</h2>

  <p class="programs">RECREATIONAL AND<br>TRAVEL TEAMS</p>
  <p class="skills">PASSING KICKING<br>SHOOTING DRIBBLING<br>BALL CONTROL</p>

  <div class="field-label">FIELD</div>
  <p class="field-address">Holloway Fenwick Middle School (4728 Meadowlark dr Silver spring, MD 20731)</p>

  <p class="register">REGISTER<br>ONLINE</p>
  <p class="site">www.valmontekickers.example</p>

  <p class="price">Registration :$210</p>
  <p class="price-note">(includes 1st month, registration, practice Uniform after 1st month.</p>
  <p class="phone">Call us Phone: (240)555-0187</p>
</main>
</body>
</html>
```